Corvale Enterprises -Business Card Design Project

I have a new logo to put onto business cards - attached
The word doc shows how I want it all laid out - front page and rear
The lettering I want is clean and rounded - modern
Reason: There was no original deadline!
Target Market(s)
25-49 year old leaders and entrepreneurs in Australia
Industry/Entity Type
Business

```html
<!DOCTYPE html>
<html lang="en">
<head>
<meta charset="utf-8">
<title>Corvale Enterprises – Business Cards</title>
<link rel="stylesheet" href="https://fonts.googleapis.com/css2?family=Questrial&family=Lato:wght@400&display=swap">
<style>
  :root {
    --backdrop: #e9e6e2;
    --card-dark: #1c1c1d;
    --card-light: #ffffff;
    --emboss: #3a3a3b;
    --brand-blue: #0d52a5;
    --brand-grey: #b9b9b9;
    --text-grey: #555555;
  }
  * { margin: 0; padding: 0; box-sizing: border-box; }
  html, body { width: 1200px; height: 800px; overflow: hidden; }
  body {
    position: relative;
    background: var(--backdrop);
    font-family: "Questrial", "Century Gothic", sans-serif;
  }
  .card {
    position: absolute;
    left: 267px;
    width: 511px;
    height: 315px;
    box-shadow: 0 2px 6px rgba(0,0,0,0.18);
  }
  .card--front { top: 98px; background: var(--card-dark); }
  .card--back { top: 427px; background: var(--card-light); }

  /* front */
  .front-brand {
    position: absolute;
    left: 86px; top: 104px;
    display: flex; align-items: center; gap: 20px;
  }
  .brand-square {
    width: 66px; height: 66px;
    background: var(--emboss);
  }
  .brand-name {
    color: var(--emboss);
    line-height: 1;
  }
  .brand-name__main { display: block; font-size: 40px; letter-spacing: 4px; }
  .brand-name__sub { display: block; font-size: 13px; letter-spacing: 9.5px; margin-top: 6px; }
  .front-tagline {
    position: absolute;
    left: 0; right: 0; top: 205px;
    text-align: center;
    font-family: "Lato", "Helvetica", sans-serif;
    font-size: 12.5px;
    color: var(--emboss);
  }

  /* back */
  .back-brand {
    position: absolute;
    left: 42px; top: 34px;
    display: flex; align-items: center; gap: 18px;
  }
  .back-brand .brand-square { width: 60px; height: 60px; background: var(--brand-grey); }
  .back-brand .brand-name { color: var(--brand-blue); }
  .back-brand .brand-name__main { font-size: 30px; letter-spacing: 3.5px; }
  .back-brand .brand-name__sub { font-size: 10px; letter-spacing: 7.4px; margin-top: 5px; }

  .services {
    position: absolute;
    left: 41px; top: 126px;
    list-style: none;
    font-size: 11.5px; line-height: 15.5px;
    color: var(--text-grey);
  }
  .person {
    position: absolute;
    right: 31px; top: 184px;
    text-align: right;
  }
  .person__name { font-size: 17px; color: var(--brand-blue); line-height: 20px; }
  .person__role { font-size: 11.5px; color: var(--text-grey); }

  .contacts {
    position: absolute;
    left: 41px; top: 232px;
    list-style: none;
    font-size: 11.5px; color: var(--text-grey);
  }
  .contacts li { display: flex; align-items: center; gap: 6px; height: 18px; }
  .contacts svg { width: 12px; height: 12px; fill: var(--brand-blue); }

  .card-band {
    position: absolute;
    left: 0; right: 0; bottom: 0;
    height: 20px;
    display: flex;
  }
  .card-band__blue { width: 299px; background: var(--brand-blue); }
  .card-band__grey { flex: 1; background: var(--brand-grey); }
</style>
</head>
<body>

<section class="card card--front" aria-label="Card front">
  <div class="front-brand">
    <div class="brand-square"></div>
    <div class="brand-name">
      <span class="brand-name__main">CORVALE</span>
      <span class="brand-name__sub">ENTERPRISES</span>
    </div>
  </div>
  <p class="front-tagline">Direction and Growth For Leaders and Entrepreneurs</p>
</section>

<section class="card card--back" aria-label="Card back">
  <div class="back-brand">
    <div class="brand-square"></div>
    <div class="brand-name">
      <span class="brand-name__main">CORVALE</span>
      <span class="brand-name__sub">ENTERPRISES</span>
    </div>
  </div>

  <ul class="services">
    <li>NLP Practitioner &amp; Coach</li>
    <li>Personal, Business &amp;Staff Development</li>
    <li>Self Resilience Programs</li>
  </ul>

  <div class="person">
    <p class="person__name">Declan Hayes</p>
    <p class="person__role">Director</p>
  </div>

  <ul class="contacts">
    <li>
      <svg viewBox="0 0 12 12" aria-hidden="true"><path d="M1 4.5C1 3 3 2 6 2s5 1 5 2.5v1H8.5V4.3C7.8 4.1 7 4 6 4s-1.8.1-2.5.3v1.2H1z"/><path d="M2.5 6.5h7L10.5 10h-9z"/></svg>
      <span>0412 555 018</span>
    </li>
    <li>
      <svg viewBox="0 0 12 12" aria-hidden="true"><path d="M1 2.5h10v7H1z M1.8 3.3 6 6.5l4.2-3.2" fill="none" stroke="#0d52a5" stroke-width="1.3"/></svg>
      <span>declan@corvaleenterprises.com.au</span>
    </li>
    <li>
      <svg viewBox="0 0 12 12" aria-hidden="true"><circle cx="6" cy="6" r="5.5"/><path d="M1 6h10M6 .5c-2.5 3-2.5 8 0 11M6 .5c2.5 3 2.5 8 0 11" fill="none" stroke="#ffffff" stroke-width="0.8"/></svg>
      <span>www.corvaleenterprises.com.au</span>
    </li>
  </ul>

  <div class="card-band">
    <div class="card-band__blue"></div>
    <div class="card-band__grey"></div>
  </div>
</section>

</body>
</html>
```